Looking for an attractive, cool poster design for our company Core Values. This would ideally be framed and placed at each company location. Would like this to be striking and memorable.

The core values that should be included on the poster are:

Be a Creator
Have an Open Mind
Do the Right Thing

The size should be standard poster size, 18 x 24, vertical orientation ideally.

The company name to include on the poster is:

Brightwave Systems Group

The design could be printed as a poster or a sticker/decal as well. Or perhaps printed on a fabric, foam boards. Versatile enough design for different output types.

Target Market(s)

Internal Team Members and visitors

Industry/Entity Type

Technology

Font styles to use
Other font styles liked:
• Montserrat

Requirements
Must have
• The design could be printed as a poster or a sticker/decal as well. Or perhaps printed on a fabric. Versatile enough design for different output types.

```html
<!DOCTYPE html>
<html lang="en">
<head>
<meta charset="utf-8">
<title>Core Values Posters – Brightwave Systems Group</title>
<link rel="stylesheet" href="https://fonts.googleapis.com/css2?family=Montserrat:wght@800&family=Oswald:wght@500&display=swap">
<style>
  :root {
    --backdrop: #c8c8ca;
    --paper: #ffffff;
    --orange: #e8902f;
    --navy: #0e4a6e;
    --rule-light: #eeeeef;
  }
  html, body {
    margin: 0;
    padding: 0;
    width: 1200px;
    height: 559px;
    overflow: hidden;
    background: var(--backdrop);
  }
  .poster-row {
    position: relative;
    width: 1200px;
    height: 559px;
  }
  .poster {
    position: absolute;
    top: 55px;
    width: 323px;
    height: 430px;
    background: var(--paper);
  }
  .poster--orange { left: 64px; }
  .poster--outline { left: 439px; }
  .poster--navy { left: 813px; }
  .poster svg { display: block; }
  .title {
    font-family: "Montserrat", sans-serif;
    font-weight: 800;
    font-size: 50px;
  }
  .value {
    font-family: "Oswald", sans-serif;
    font-weight: 500;
    font-size: 40px;
  }
  .company {
    font-family: "Montserrat", sans-serif;
    font-weight: 800;
    font-size: 9px;
  }
  .poster--orange .title,
  .poster--orange .value { fill: var(--orange); }
  .poster--orange .divider { fill: var(--orange); }
  .poster--orange .company,
  .poster--orange .company-dot { fill: var(--navy); }

  .poster--navy .title,
  .poster--navy .value,
  .poster--navy .divider,
  .poster--navy .company,
  .poster--navy .company-dot { fill: var(--navy); }

  .poster--outline .title { fill: none; stroke: var(--orange); stroke-width: 0.7; }
  .poster--outline .value { fill: none; stroke: var(--navy); stroke-width: 0.7; }
  .poster--outline .divider { fill: var(--rule-light); }
  .poster--outline .company,
  .poster--outline .company-dot { fill: var(--orange); }
</style>
</head>
<body>
<main class="poster-row">
  <section class="poster poster--orange" aria-label="Core values poster, orange">
    <svg width="323" height="430" viewBox="0 0 323 430">
      <text class="title" transform="translate(78,365) rotate(-90)" textLength="311" lengthAdjust="spacingAndGlyphs">CORE VALUES</text>
      <rect class="divider" x="85" y="54" width="3.5" height="309" rx="1.5"/>
      <text class="value" x="100" y="84" textLength="64" lengthAdjust="spacingAndGlyphs">BE A</text>
      <text class="value" x="100" y="129" textLength="131" lengthAdjust="spacingAndGlyphs">CREATOR</text>
      <text class="value" x="100" y="199" textLength="122" lengthAdjust="spacingAndGlyphs">HAVE AN</text>
      <text class="value" x="100" y="244" textLength="162" lengthAdjust="spacingAndGlyphs">OPEN MIND</text>
      <text class="value" x="100" y="317" textLength="103" lengthAdjust="spacingAndGlyphs">DO THE</text>
      <text class="value" x="100" y="361" textLength="186" lengthAdjust="spacingAndGlyphs">RIGHT THING</text>
      <circle class="company-dot" cx="113" cy="405" r="5"/>
      <text class="company" x="124" y="408.5">BRIGHTWAVE SYSTEMS GROUP</text>
    </svg>
  </section>

  <section class="poster poster--outline" aria-label="Core values poster, outline">
    <svg width="323" height="430" viewBox="0 0 323 430">
      <text class="title" transform="translate(78,365) rotate(-90)" textLength="311" lengthAdjust="spacingAndGlyphs">CORE VALUES</text>
      <rect class="divider" x="85" y="54" width="3.5" height="309" rx="1.5"/>
      <text class="value" x="100" y="84" textLength="64" lengthAdjust="spacingAndGlyphs">BE A</text>
      <text class="value" x="100" y="129" textLength="131" lengthAdjust="spacingAndGlyphs">CREATOR</text>
      <text class="value" x="100" y="199" textLength="122" lengthAdjust="spacingAndGlyphs">HAVE AN</text>
      <text class="value" x="100" y="244" textLength="162" lengthAdjust="spacingAndGlyphs">OPEN MIND</text>
      <text class="value" x="100" y="317" textLength="103" lengthAdjust="spacingAndGlyphs">DO THE</text>
      <text class="value" x="100" y="361" textLength="186" lengthAdjust="spacingAndGlyphs">RIGHT THING</text>
      <circle class="company-dot" cx="115" cy="405" r="3"/>
      <text class="company" x="124" y="408.5">BRIGHTWAVE SYSTEMS GROUP</text>
    </svg>
  </section>

  <section class="poster poster--navy" aria-label="Core values poster, navy">
    <svg width="323" height="430" viewBox="0 0 323 430">
      <text class="title" transform="translate(78,365) rotate(-90)" textLength="311" lengthAdjust="spacingAndGlyphs">CORE VALUES</text>
      <rect class="divider" x="85" y="54" width="3.5" height="309" rx="1.5"/>
      <text class="value" x="100" y="84" textLength="64" lengthAdjust="spacingAndGlyphs">BE A</text>
      <text class="value" x="100" y="129" textLength="131" lengthAdjust="spacingAndGlyphs">CREATOR</text>
      <text class="value" x="100" y="199" textLength="122" lengthAdjust="spacingAndGlyphs">HAVE AN</text>
      <text class="value" x="100" y="244" textLength="162" lengthAdjust="spacingAndGlyphs">OPEN MIND</text>
      <text class="value" x="100" y="317" textLength="103" lengthAdjust="spacingAndGlyphs">DO THE</text>
      <text class="value" x="100" y="361" textLength="186" lengthAdjust="spacingAndGlyphs">RIGHT THING</text>
      <circle class="company-dot" cx="113" cy="405" r="5"/>
      <text class="company" x="124" y="408.5">BRIGHTWAVE SYSTEMS GROUP</text>
    </svg>
  </section>
</main>
</body>
</html>
```